Corrigan & Hale, LLC
Business Cards & Stationery
Corrigan & Hale, LLC -
Creative Brief
Professional
Deborah L. Corrigan
Attorney At Law
418 W. Brookfield Avenue Suite 3B Pearl River, New York 10965-2274
dcorrigan@corriganandhale-example.com
www.corriganandhale-example.com
We will need to be able to use template for other people in the firm.
Specializing in Civil Litigation, Wills, Trusts & Estates, Guardianships, and related matters

```html
<!DOCTYPE html>
<html lang="en">
<head>
<meta charset="utf-8">
<title>Corrigan &amp; Hale, LLC — Business Card</title>
<link href="https://fonts.googleapis.com/css2?family=Crimson+Pro:ital,wght@0,400;0,600;1,700&display=swap" rel="stylesheet">
<style>
  :root {
    --backdrop: #e9e7e3;
    --card: #ffffff;
    --green: #1f6b35;
    --grey-arc: #8c8c8c;
    --ink: #3a3a3a;
    --rule: #b9b9b9;
  }
  * { box-sizing: border-box; margin: 0; padding: 0; }
  html, body {
    width: 1200px; height: 780px; overflow: hidden;
    background: var(--backdrop);
    font-family: "Crimson Pro", Georgia, serif;
  }
  .card {
    position: absolute; left: 100px; top: 104px;
    width: 1000px; height: 572px;
    background: var(--card);
    border-radius: 28px;
    overflow: hidden;
    box-shadow: 0 10px 30px rgba(0,0,0,0.18);
  }
  .card-swooshes { position: absolute; inset: 0; }
  .brand { position: absolute; left: 250px; top: 112px; display: flex; align-items: center; gap: 22px; }
  .brand-mark { width: 84px; height: 84px; background: var(--green); }
  .brand-name {
    font-size: 54px; font-weight: 600; font-variant: small-caps;
    color: var(--green); letter-spacing: 1px; line-height: 1;
  }
  .brand-rule {
    position: absolute; left: 360px; top: 200px; width: 560px; height: 2px;
    background: var(--rule);
  }
  .brand-tagline {
    position: absolute; left: 560px; top: 208px;
    font-size: 22px; font-weight: 600; color: var(--green);
    letter-spacing: 4px; text-transform: uppercase;
  }
  .person {
    position: absolute; right: 530px; top: 298px; text-align: right;
    color: var(--ink); font-size: 22px; line-height: 1.3;
  }
  .person-name { font-size: 36px; font-weight: 700; font-style: italic; color: var(--green); line-height: 1.2; }
  .divider {
    position: absolute; left: 492px; top: 300px; width: 2px; height: 200px;
    background: var(--rule);
  }
  .contact { position: absolute; left: 512px; top: 292px; list-style: none; }
  .contact li {
    display: flex; align-items: center; gap: 12px;
    font-size: 21px; color: var(--ink); height: 38px;
  }
  .contact svg { width: 22px; height: 22px; flex: none; }
</style>
</head>
<body>
  <div class="card">
    <svg class="card-swooshes" viewBox="0 0 1000 572" aria-hidden="true">
      <path d="M0,0 H250 Q70,70 0,380 Z" fill="var(--green)"/>
      <path d="M268,0 Q85,80 0,410" fill="none" stroke="var(--grey-arc)" stroke-width="7"/>
      <path d="M1000,572 H770 Q940,520 1000,300 Z" fill="var(--green)"/>
      <path d="M748,572 Q925,510 1000,272" fill="none" stroke="var(--grey-arc)" stroke-width="7"/>
    </svg>

    <div class="brand">
      <div class="brand-mark"></div>
      <div class="brand-name">Corrigan &amp; Hale, LLC</div>
    </div>
    <div class="brand-rule"></div>
    <div class="brand-tagline">Attorneys at Law</div>

    <div class="person">
      <p class="person-name">Deborah L. Corrigan</p>
      <p>Attorney At Law</p>
      <p>418 W. Brookfield Avenue</p>
      <p>Suite 3B, Ashford Glen</p>
      <p>New York 10990-2274</p>
    </div>

    <div class="divider"></div>

    <ul class="contact">
      <li>
        <svg viewBox="0 0 24 24"><path fill="var(--green)" d="M6.6 10.8a15.2 15.2 0 0 0 6.6 6.6l2.2-2.2a1 1 0 0 1 1-.25 11.4 11.4 0 0 0 3.6.57 1 1 0 0 1 1 1V20a1 1 0 0 1-1 1A17 17 0 0 1 3 4a1 1 0 0 1 1-1h3.5a1 1 0 0 1 1 1c0 1.25.2 2.450.57 3.57a1 1 0 0 1-.25 1z"/></svg>
        555.410.2836
      </li>
      <li>
        <svg viewBox="0 0 24 24"><rect x="6" y="3" width="12" height="6" fill="var(--green)"/><rect x="3" y="9" width="18" height="9" rx="2" fill="var(--green)"/><rect x="6" y="15" width="12" height="6" fill="#fff" stroke="var(--green)" stroke-width="2"/></svg>
        555.410.2837
      </li>
      <li>
        <svg viewBox="0 0 24 24"><circle cx="12" cy="12" r="4" fill="none" stroke="var(--green)" stroke-width="2.5"/><path d="M16 8v5a2.5 2.5 0 0 0 5 0v-1a9 9 0 1 0-4 7.5" fill="none" stroke="var(--green)" stroke-width="2.5"/></svg>
        dcorrigan@corriganandhale-example.com
      </li>
      <li>
        <svg viewBox="0 0 24 24"><circle cx="12" cy="12" r="10" fill="var(--green)"/><path d="M2 12h20M12 2c3 3 3 17 0 20M12 2c-3 3-3 17 0 20" fill="none" stroke="#fff" stroke-width="1.5"/></svg>
        www.corriganandhale-example.com
      </li>
    </ul>
  </div>
</body>
</html>
```